Business Card and Simple Logo Desgin

New Zealand based start up company "Brook Advisory LTD" requires business cards and simple logo design.

Card Content.

Brook Advisory LTD

Joanna Pritchard
CA, BMS (Hons)

j.pritchard@brookadvisory.co.nz
PH +64 21 574 160

Target Market(s)

Corporate Business in IT, Finance and accounting.

Industry/Entity Type

Business

```html
<!DOCTYPE html>
<html lang="en">
<head>
<meta charset="utf-8">
<title>Brook Advisory LTD – Business Card</title>
<link href="https://fonts.googleapis.com/css2?family=Oswald:wght@400&family=Arimo:wght@400;700&display=swap" rel="stylesheet">
<style>
  :root {
    --page: #ffffff;
    --blue-light: #1b84cc;
    --blue-mid: #0f5ea6;
    --blue-dark: #0b3f7a;
    --orange: #f7a93b;
    --grey-text: #58595b;
    --white: #ffffff;
    --shadow: rgba(0, 0, 0, 0.45);
  }
  html, body {
    margin: 0;
    padding: 0;
    width: 1200px;
    height: 901px;
    overflow: hidden;
    background: var(--page);
  }
  .canvas {
    position: relative;
    width: 1200px;
    height: 901px;
  }
  .card {
    position: absolute;
    left: 260px;
    width: 636px;
    height: 364px;
    overflow: hidden;
    box-shadow: 4px 5px 7px var(--shadow);
  }
  /* Front */
  .card-front {
    top: 60px;
    background: radial-gradient(circle at 62% 38%, var(--blue-light) 0%, var(--blue-mid) 45%, var(--blue-dark) 100%);
  }
  .front-mark {
    position: absolute;
    left: 60px;
    top: 96px;
    width: 150px;
    height: 150px;
    background: var(--orange);
  }
  .front-company {
    position: absolute;
    left: 296px;
    top: 150px;
    margin: 0;
    font-family: "Oswald", sans-serif;
    font-weight: 400;
    font-size: 34px;
    line-height: 1;
    color: #e6ecf3;
    letter-spacing: 0.3px;
  }
  .front-web {
    position: absolute;
    right: 80px;
    top: 370px;
    top: 309px;
    font-family: "Oswald", sans-serif;
    font-size: 17px;
    line-height: 1;
    color: var(--white);
    letter-spacing: 1px;
  }
  .front-web .accent { color: var(--orange); }

  /* Back */
  .card-back {
    top: 496px;
    background: var(--white);
  }
  .back-wave {
    position: absolute;
    inset: 0;
    width: 636px;
    height: 364px;
  }
  .back-mark {
    position: absolute;
    left: 134px;
    top: 44px;
    width: 70px;
    height: 70px;
    background: var(--orange);
  }
  .back-company {
    position: absolute;
    left: 36px;
    top: 146px;
    margin: 0;
    font-family: "Oswald", sans-serif;
    font-weight: 400;
    font-size: 37px;
    line-height: 1;
    color: var(--grey-text);
  }
  .contact {
    position: absolute;
    right: 40px;
    top: 232px;
    text-align: right;
    font-family: "Arimo", sans-serif;
    color: var(--white);
  }
  .contact-name {
    margin: 0;
    font-weight: 700;
    font-size: 20px;
    line-height: 24px;
    color: var(--orange);
  }
  .contact-title {
    margin: 0 0 14px;
    font-size: 16px;
    line-height: 20px;
  }
  .contact-line {
    display: flex;
    justify-content: flex-end;
    align-items: center;
    gap: 8px;
    margin: 0;
    font-size: 16px;
    line-height: 21px;
  }
  .contact-icon {
    width: 12px;
    height: 12px;
    flex: none;
  }
  .edge-tab {
    position: absolute;
    right: 0;
    top: 217px;
    width: 12px;
    height: 114px;
    background: var(--orange);
    border-radius: 8px 0 0 8px;
  }
</style>
</head>
<body>
<main class="canvas">

  <section class="card card-front" aria-label="Card front">
    <div class="front-mark"></div>
    <h1 class="front-company">Brook Advisory LTD</h1>
    <p class="front-web" style="margin:0">www.brook<span class="accent">advisory</span>.co.nz</p>
  </section>

  <section class="card card-back" aria-label="Card back">
    <svg class="back-wave" viewBox="0 0 636 364" aria-hidden="true">
      <defs>
        <linearGradient id="backBlue" x1="1" y1="0" x2="0" y2="1">
          <stop offset="0" stop-color="#1b84cc"/>
          <stop offset="0.55" stop-color="#0f5ea6"/>
          <stop offset="1" stop-color="#0b3f7a"/>
        </linearGradient>
      </defs>
      <path d="M0,218 C90,330 260,345 400,175 C480,80 560,60 636,66 L636,364 L0,364 Z" fill="var(--orange)"/>
      <path d="M0,238 C90,348 262,362 405,195 C485,100 562,80 636,84 L636,364 L0,364 Z" fill="url(#backBlue)"/>
    </svg>

    <div class="back-mark"></div>
    <h2 class="back-company">Brook Advisory LTD</h2>

    <div class="contact">
      <p class="contact-name">Joanna Pritchard</p>
      <p class="contact-title">CA, BMS (Hons)</p>
      <p class="contact-line">+64 21 574 160
        <svg class="contact-icon" viewBox="0 0 12 12" aria-hidden="true"><rect x="3" y="0.5" width="6" height="11" rx="1.2" fill="none" stroke="#f7a93b" stroke-width="1.4"/><rect x="4.6" y="9" width="2.8" height="1" fill="#f7a93b"/></svg>
      </p>
      <p class="contact-line">j.pritchard@brookadvisory.co.nz
        <svg class="contact-icon" viewBox="0 0 12 12" aria-hidden="true"><rect x="0.5" y="2.5" width="11" height="7.5" fill="#f7a93b"/><path d="M0.5,2.5 L6,7 L11.5,2.5" fill="none" stroke="#0f5ea6" stroke-width="1"/></svg>
      </p>
    </div>

    <div class="edge-tab"></div>
  </section>

</main>
</body>
</html>
```